Business card design needed

We are a start up Mobile Vet Clinic.
We will be servicing an are that cover the Gladstone Region Shire.
Bookings will be made via the number listed or email address.
Travel will be charged

Target Market(s)

Pet Owners

Industry/Entity Type

Business

Contact Information for Business Card

BRINDELLA MOBILE VET
Tarrowen Pty Ltd
Dana Fosterby BVSc
27 Wexhaven St
Yarrowgap QLD 4682

PH: 0743186209 Fax: 0743186514 email: bmvet@quillnet.example

Logo styles of interest
Pictorial/Combination Logo

```html
<!DOCTYPE html>
<html lang="en">
<head>
<meta charset="utf-8">
<title>Brindella Mobile Vet – Business Card</title>
<link rel="stylesheet" href="https://fonts.googleapis.com/css2?family=Source+Sans+3:wght@400;500&display=swap">
<style>
  :root {
    --card-bg: #ffffff;
    --brand-blue: #2aa8e0;
    --brand-blue-soft: #5bbde9;
    --text-blue: #1f7cba;
    --rule-start: #2aa8e0;
    --rule-end: #d6eefa;
  }
  html, body {
    margin: 0;
    padding: 0;
    width: 1200px;
    height: 667px;
    overflow: hidden;
    background: var(--card-bg);
  }
  .card {
    position: relative;
    width: 1200px;
    height: 667px;
    background: var(--card-bg);
    font-family: "Source Sans 3", sans-serif;
  }
  .brand {
    position: absolute;
    left: 96px;
    top: 154px;
    margin: 0;
    font-family: "Source Sans 3", sans-serif;
    font-weight: 500;
    font-size: 62px;
    line-height: 1;
    letter-spacing: 3.5px;
    color: var(--brand-blue);
    white-space: nowrap;
  }
  .brand-mark {
    position: absolute;
    left: 1030px;
    top: 96px;
    width: 150px;
    height: 150px;
  }
  .brand-rule {
    position: absolute;
    left: 98px;
    top: 276px;
    width: 680px;
    height: 2px;
    background: linear-gradient(90deg, var(--rule-start), var(--rule-end));
  }
  .contact {
    position: absolute;
    left: 98px;
    top: 334px;
    margin: 0;
    font-style: normal;
    font-weight: 400;
    font-size: 39px;
    line-height: 51.6px;
    letter-spacing: 2.5px;
    color: var(--text-blue);
  }
  .contact span { display: block; white-space: nowrap; }
</style>
</head>
<body>
  <main class="card">
    <h1 class="brand">BRINDELLA MOBILE VET</h1>
    <svg class="brand-mark" viewBox="0 0 150 150" aria-hidden="true">
      <circle cx="75" cy="75" r="72" fill="var(--brand-blue-soft)"/>
    </svg>
    <div class="brand-rule"></div>
    <address class="contact">
      <span>Tarrowen Pty Ltd Dana Fosterby BVSc</span>
      <span>27 Wexhaven St Yarrowgap</span>
      <span>QLD 4682 PH: 0743186209</span>
      <span>Fax: 0743186514</span>
      <span>email: bmvet@quillnet.example</span>
    </address>
  </main>
</body>
</html>
```